CopperField Lantern and Nine Lamps Over Driftwood

Create a book cover for Dario Pelletvane first biography and a self-help book about Nine Lamps Over Driftwood.

US Pelican Sentry uses his battlefield and transition experience to guide you to success in any life challenge.

Back Cover:
Every single human being will go through a life changing event. It could be losing a job of 20 years, a divorce, being an athlete and getting hurt, or retiring from the military. These life changing events can sometime cause disastrous effects on us, our relationships, and some people never recover. This happened to Dario when he left a 12 year carrier as a Pelican Sentry with Pelican Field Group. He then took the skills he learned as a Sentry and got to work solving the problem.

The Copperfield Lantern takes us through a journey of Dario’s Transition out of Field Group as he attempts to reintegrate in to civilian life. Through this Journey he found 7 different stages of transition and this book outlines them and what you can do about.

Target Market(s)

Military, Veterans

Industry/Entity Type

Military

Font styles to use
Other font styles liked:
• Bebas Neu

Colors

Designer to choose colors to be used in the design.

Requirements
Must have
• Must have the cover image title, and my name.
• US Pelican Sentry uses his battlefield and transition experience to guide you to success in any life challenge.
Nice to have
• Would be nice to fit the device in the design somewhere maybe next to my name if it fits well.
• Back Cover:
• Every single human being will go through a life changing event. It could be losing a job of 20 years, a divorce, being an athlete and getting hurt, or retiring from the military. These life changing events can sometime cause disastrous effects on us, our relationships, and some people never recover. This happened to Dario when he left a 12 year carrier as a Pelican Sentry with Pelican Field Group. He then took the skills he learned as a Sentry and got to work solving the problem.
• The Copperfield Lantern takes us through a journey of Dario’s Transition out of Field Group as he attempts to reintegrate in to civilian life. Through this Journey he found 7 different stages of transition and this book outlines them and what you can do about.
Should not have
• No Pelican compass and trowel.

```html
<!DOCTYPE html>
<html lang="en">
<head>
<meta charset="utf-8">
<title>The Copperfield Lantern – Book Covers</title>
<link rel="stylesheet" href="https://fonts.googleapis.com/css2?family=Bebas+Neue&display=swap">
<style>
  :root {
    --page-bg: #ffffff;
    --sepia-light: #d6c3ad;
    --sepia-mid: #a5876a;
    --sepia-dark: #5a4232;
    --banner-red: #ee2722;
    --banner-ink: #2b1812;
    --back-dark: #1a120a;
    --back-brown: #46320f;
    --back-text: #f3efe8;
    --title-red: #e8261f;
    --spine-gold: #8a7a1e;
    --front-text: #2b1812;
  }
  * { box-sizing: border-box; margin: 0; padding: 0; }
  html, body {
    width: 1200px; height: 1200px; overflow: hidden;
    background: var(--page-bg);
    font-family: "Bebas Neue", "Oswald", sans-serif;
  }
  .book-pair { position: relative; width: 1200px; height: 1200px; }
  .cover {
    position: absolute; top: 230px; width: 540px; height: 700px;
    overflow: hidden;
    border-left: 6px solid var(--spine-gold);
    box-shadow: 0 10px 30px rgba(0,0,0,0.18);
  }
  .cover--front { left: 40px; }
  .cover--back { left: 620px; }

  /* Front cover */
  .front-photo {
    position: absolute; inset: 0;
    background:
      linear-gradient(180deg, rgba(90,66,50,0) 35%, rgba(90,66,50,0.55) 100%),
      linear-gradient(150deg, var(--sepia-light) 0%, #c4ab92 50%, var(--sepia-mid) 100%);
  }
  .front-title {
    position: absolute; left: 34px; right: 34px; top: 34px;
    color: var(--front-text);
    font-size: 60px; line-height: 0.9; letter-spacing: 0.5px;
  }
  .name-banner {
    position: absolute; left: 230px; right: 0; top: 420px; height: 84px;
    background: var(--banner-red);
    padding: 14px 0 0 26px;
    color: var(--banner-ink);
  }
  .name-banner::before {
    content: ""; position: absolute; left: -10px; top: -4px; bottom: -4px;
    width: 5px; background: var(--banner-ink);
  }
  .author-name { font-size: 38px; line-height: 0.95; letter-spacing: 0.5px; font-weight: 400; }
  .book-tag { font-size: 19px; line-height: 1; }
  .front-tagline {
    position: absolute; left: 34px; right: 34px; bottom: 30px;
    color: var(--back-text);
    font-size: 22px; line-height: 1.1; letter-spacing: 0.3px;
  }

  /* Back cover */
  .back-photo {
    position: absolute; inset: 0;
    background:
      radial-gradient(ellipse at 40% 30%, var(--back-brown) 0%, transparent 55%),
      radial-gradient(ellipse at 70% 80%, #3a2a12 0%, transparent 50%),
      var(--back-dark);
  }
  .back-copy {
    position: absolute; left: 52px; right: 48px; top: 150px;
    color: var(--back-text);
    font-size: 22px; line-height: 1.1; text-transform: uppercase;
  }
  .back-copy p + p { margin-top: 24px; }
  .back-title {
    display: block;
    color: var(--title-red); font-size: 44px; line-height: 0.95;
    margin-bottom: 4px;
  }
</style>
</head>
<body>
<main class="book-pair">
  <section class="cover cover--front">
    <div class="front-photo" role="img" aria-label="Sepia portrait of a bearded operator in sunglasses and plate carrier, with a larger faded portrait in the background"></div>
    <h2 class="front-title">The Copperfield Lantern</h2>
    <div class="name-banner">
      <h1 class="author-name">Dario Pelletvane</h1>
      <div class="book-tag">First Biography</div>
    </div>
    <p class="front-tagline">US Pelican Sentry uses his battlefield and transition experience to guide you to success in any life challenge.</p>
  </section>

  <section class="cover cover--back">
    <div class="back-photo" role="img" aria-label="Dark brown close-up photo of tactical gear"></div>
    <div class="back-copy">
      <p>Every single human being will go through a life changing event. It could be losing a job of 20 years, a divorce, being an athlete and getting hurt, or retiring from the military. These life changing events can sometime cause disastrous effects on us, our relationships, and some people never recover. This happened to Dario when he left a 12 year carrier as a Pelican Sentry with Pelican Field Group. He then took the skills he learned as a Sentry and got to work solving the problem.</p>
      <p><span class="back-title">The Copperfield Lantern</span>takes us through a journey of Dario’s transition out of Field Group as he attempts to reintegrate in to civilian life. Through this journey he found 7 different stages of transition and this book outlines them and what you can do about.</p>
    </div>
  </section>
</main>
</body>
</html>
```